Verdant Loop Advisors, LLC

I am looking for a simple, clear layout with my logo prominent and embossed, on the best quality card stock available. I would like the business name and phone number included on the card as well......I dont want my name anywhere on the card and I would like my logo embossed on the card......something simple with a white back......open to designs as long as they go along with recycling symbols and green type stuff.....The address, website, cell number, fax number, and email are listed below

5374 Tillbury Fenwood Road
Hyattsville, MD 20785

c. 240.555.0143 f. 240.555.0187
e. sales@verdantloopadvisors.example
w. www.verdantloopadvisors.example

Industry/Entity Type

Recycling

```html
<!DOCTYPE html>
<html lang="en">
<head>
<meta charset="utf-8">
<title>Verdant Loop Advisors, LLC — Business Card</title>
<link href="https://fonts.googleapis.com/css2?family=Montserrat:wght@600;700&display=swap" rel="stylesheet">
<style>
  :root {
    --backdrop: #e9e7e3;
    --card: #f8f8f4;
    --ink: #141414;
    --green: #2f7d3a;
    --green-soft: #cfe3c6;
    --green-mid: #9cc98a;
  }
  * { box-sizing: border-box; margin: 0; padding: 0; }
  html, body {
    width: 1200px; height: 1000px; overflow: hidden;
    background: var(--backdrop);
    font-family: "Montserrat", Arial, sans-serif;
    color: var(--ink);
  }
  .card {
    position: absolute; left: 100px; top: 214px;
    width: 1000px; height: 572px;
    background: var(--card);
    box-shadow: 0 6px 22px rgba(0,0,0,.18);
  }
  .brand {
    position: absolute; left: 64px; top: 70px;
    display: flex; align-items: center; gap: 18px;
  }
  .brand-mark {
    width: 58px; height: 58px; background: var(--green);
  }
  .brand-name {
    font-weight: 700; font-size: 40px; letter-spacing: .5px;
    color: var(--ink); line-height: 1;
  }
  .artwork {
    position: absolute; left: 700px; top: 150px;
    width: 260px; height: 340px;
    background: linear-gradient(180deg, var(--green-soft) 0%, var(--green-mid) 100%);
  }
  .address {
    position: absolute; left: 72px; top: 300px;
    font-style: normal;
    font-weight: 700; font-size: 30px; line-height: 1.3;
  }
  .contacts {
    position: absolute; left: 72px; top: 400px;
    list-style: none;
    font-weight: 600; font-size: 28px; line-height: 1.5;
  }
  .contacts li { display: flex; align-items: center; gap: 10px; }
  .contacts svg { width: 24px; height: 24px; fill: var(--green); flex: none; }
  .contacts .gap { margin-left: 16px; }
</style>
</head>
<body>
  <main class="card">
    <header class="brand">
      <span class="brand-mark"></span>
      <span class="brand-name">Verdant Loop Advisors, LLC</span>
    </header>

    <div class="artwork" role="img" aria-label="Illustration area: a tree growing from soil inside circling recycling arrows"></div>

    <address class="address">
      5374 Tillbury Fenwood Road<br>
      Hyattsville, MD 20785
    </address>

    <ul class="contacts">
      <li>
        <svg viewBox="0 0 24 24" aria-label="Cell"><path d="M7 1h10a2 2 0 0 1 2 2v18a2 2 0 0 1-2 2H7a2 2 0 0 1-2-2V3a2 2 0 0 1 2-2zm0 3v14h10V4zm5 15.5a1.2 1.2 0 1 0 0 2.4 1.2 1.2 0 0 0 0-2.4z"/></svg>
        240.555.0143
        <svg class="gap" viewBox="0 0 24 24" aria-label="Fax"><path d="M6 2h9l3 3v4h2a2 2 0 0 1 2 2v9a2 2 0 0 1-2 2H4a2 2 0 0 1-2-2v-9a2 2 0 0 1 2-2h2zm2 2v5h8V6h-2V4zM6 13v2h2v-2zm4 0v2h2v-2zm4 0v2h4v-2zm-8 4v2h2v-2zm4 0v2h2v-2z"/></svg>
        240.555.0187
      </li>
      <li>
        <svg viewBox="0 0 24 24" aria-label="Email"><path d="M2 5h20v14H2zm2 2v.5l8 5.5 8-5.5V7z"/></svg>
        sales@verdantloopadvisors.example
      </li>
      <li>
        <svg viewBox="0 0 24 24" aria-label="Website"><path d="M12 2a10 10 0 1 0 0 20 10 10 0 0 0 0-20zm1 2.1c1.3.5 2.4 2.4 2.9 4.9H13zm-2 0V9H8.1c.5-2.5 1.6-4.4 2.9-4.9zM4.3 11h3.6a19 19 0 0 0 0 2H4.3a8 8 0 0 1 0-2zm5.7 0h1v2h-1a17 17 0 0 1 0-2zm3 0h1a17 17 0 0 1 0 2h-1zm3.1 0h3.6a8 8 0 0 1 0 2h-3.6a19 19 0 0 0 0-2zM8.1 15H11v4.9c-1.3-.5-2.4-2.4-2.9-4.9zM13 15h2.9c-.5 2.5-1.6 4.4-2.9 4.9z"/></svg>
        www.verdantloopadvisors.example
      </li>
    </ul>
  </main>
</body>
</html>
```